Vexora.app is a developing company for entrepreneurs who need legal services.

Our Company Slogan is : The Only Path You Want
Company Info:
Vexora is built to help anyone sort through the confusion of taking an idea from thoughts to a tangible reality, legally. We are here to help make the incorporation, idea protection and any other legal necessities an after thought for you. If you know your idea is the next Pindleco we will help you make the right legal decisions from the start.
Subscription Model packages: 2.99, 4.99, 9.99 options in three separate boxes. Choose a monthly option and get started with your startups legal services. Start Now!
Follow us on Social: @vexora.app
Website template look:
Build an app landing page for the company. Need a clean subscription based template with my updated logo and color scheme to create a landing page, team, and contact page. I want to be able to edit the copy. Very simple and clean using company colors.
Target Market(s)
Gen-Z or Millenial aged entrepreneurs starting a business for the first time.
Industry/Entity Type
Legal
Coding
Coded - Design and coding required
Number of Pages Required
3 page
Font styles to use
Other font styles liked:
- Roboto, or Museo Sans 300,700
Look and feel

```html
<!DOCTYPE html>
<html lang="en">
<head>
<meta charset="utf-8">
<title>Vexora – The Only Path You Want</title>
<link rel="stylesheet" href="https://fonts.googleapis.com/css2?family=Fira+Sans:wght@300;400;500;700&display=swap">
<style>
  :root {
    --blue: #3bb0e6;
    --sky: #37b5f9;
    --green: #9bc95a;
    --teal: #5dbfb6;
    --ink: #333333;
    --page: #f6f6f4;
    --white: #ffffff;
    --rule: #e6e6e6;
  }
  * { margin: 0; padding: 0; box-sizing: border-box; }
  html, body { width: 994px; height: 1200px; overflow: hidden; }
  body {
    position: relative;
    background: var(--page);
    font-family: "Fira Sans", Arial, sans-serif;
    color: var(--ink);
  }
  .site-header {
    position: absolute; left: 0; top: 0; width: 994px; height: 88px;
    background: var(--white);
  }
  .brand {
    position: absolute; left: 125px; top: 27px;
    display: flex; align-items: center; gap: 8px;
  }
  .brand-dot { width: 24px; height: 24px; border-radius: 50%; background: var(--blue); }
  .brand-text { display: flex; flex-direction: column; }
  .brand-name { font-size: 20px; font-weight: 700; color: var(--blue); letter-spacing: 0.5px; line-height: 1; }
  .brand-tagline { font-size: 7px; color: var(--ink); letter-spacing: 1px; margin-top: 2px; }
  .main-nav { position: absolute; top: 36px; left: 665px; display: flex; gap: 24px; }
  .main-nav a { font-size: 13px; color: var(--ink); text-decoration: none; }
  .main-nav a.is-active { color: var(--blue); }

  .hero {
    position: absolute; left: 0; top: 88px; width: 994px; height: 415px;
    background: linear-gradient(100deg, #3eb1e0 0%, var(--teal) 45%, #7fc68c 75%, var(--green) 100%);
    clip-path: polygon(0 0, 100% 0, 100% 100%, 0 87.5%);
  }
  .hero-photo {
    position: absolute; left: 100px; top: 0; width: 420px; height: 415px;
    background: radial-gradient(ellipse at 50% 45%, rgba(40,110,120,0.25), rgba(40,110,120,0) 70%);
  }
  .hero-title {
    position: absolute; left: 125px; top: 104px; width: 340px;
    font-size: 28px; font-weight: 300; line-height: 33px; color: var(--white); letter-spacing: 0.3px;
  }
  .hero-lead {
    position: absolute; left: 125px; top: 191px; width: 320px;
    font-size: 12px; font-weight: 300; line-height: 16px; color: var(--white);
  }
  .hero-rule { position: absolute; left: 125px; top: 244px; width: 265px; height: 1px; background: rgba(255,255,255,0.7); }
  .hero-button {
    position: absolute; left: 125px; top: 271px; width: 125px; height: 35px;
    border: 1px solid var(--white); border-radius: 3px;
    display: flex; align-items: center; justify-content: center;
    font-size: 13px; font-weight: 700; color: var(--white);
  }
  .app-preview {
    position: absolute; left: 615px; top: 143px; width: 192px; height: 350px;
    border: 6px solid #1d1d1d; border-radius: 28px 28px 0 0; border-bottom: 0;
    background: linear-gradient(180deg, var(--green) 0%, #6cc09e 50%, var(--sky) 100%);
  }

  .about { position: absolute; left: 0; top: 545px; width: 994px; text-align: center; }
  .about-title { font-size: 27px; font-weight: 300; color: var(--blue); letter-spacing: 0.5px; }
  .about-text { margin: 14px auto 0; width: 720px; font-size: 12.7px; line-height: 20px; color: var(--ink); }

  .plans { position: absolute; top: 723px; left: 0; width: 994px; }
  .plan-card {
    position: absolute; top: 0; width: 226px; height: 278px;
    background: var(--white); border-radius: 3px; text-align: center;
    box-shadow: 0 10px 18px rgba(0,0,0,0.08);
  }
  .plan-card:nth-child(1) { left: 122px; }
  .plan-card:nth-child(2) { left: 384px; }
  .plan-card:nth-child(3) { left: 642px; }
  .plan-price { margin-top: 26px; font-size: 17px; color: var(--blue); }
  .plan-rule { margin: 12px 22px 0; height: 1px; background: var(--rule); }
  .plan-text { margin-top: 25px; font-size: 13px; line-height: 20px; color: var(--ink); }
  .plan-term { margin-top: 32px; font-size: 12.5px; color: var(--blue); }
  .plan-button {
    display: flex; align-items: center; justify-content: center;
    margin: 19px auto 0; width: 100px; height: 28px; border-radius: 3px;
    background: var(--green); color: var(--white); font-size: 12px; font-weight: 300;
  }

  .site-footer { position: absolute; left: 0; top: 1076px; width: 994px; height: 124px; background: var(--sky); }
  .footer-brand { position: absolute; left: 125px; top: 27px; display: flex; flex-direction: column; align-items: center; gap: 8px; }
  .footer-brand-dot { width: 34px; height: 34px; border-radius: 50%; background: var(--white); }
  .footer-brand-name { font-size: 20px; font-weight: 700; color: var(--white); letter-spacing: 0.5px; }
  .footer-nav { position: absolute; left: 413px; top: 24px; width: 108px; }
  .footer-nav a {
    display: block; height: 29px; padding-top: 2px;
    font-size: 12.5px; color: var(--white); text-decoration: none;
  }
  .footer-nav a:not(:last-child) { border-bottom: 1px solid rgba(255,255,255,0.8); margin-bottom: 4px; }
  .social { position: absolute; left: 750px; top: 35px; }
  .social-label { font-size: 12.5px; color: var(--white); }
  .social-links { display: flex; gap: 7px; margin-top: 16px; }
  .social-links span { width: 25px; height: 25px; border-radius: 50%; background: rgba(255,255,255,0.35); }
  .social-links span.is-active { background: var(--white); }
</style>
</head>
<body>
  <header class="site-header">
    <div class="brand">
      <span class="brand-dot"></span>
      <span class="brand-text">
        <span class="brand-name">Vexora</span>
        <span class="brand-tagline">The Only Path You Want</span>
      </span>
    </div>
    <nav class="main-nav">
      <a href="#">Home</a>
      <a href="#" class="is-active">Our Team</a>
      <a href="#">Contact Us</a>
    </nav>
  </header>

  <section class="hero">
    <div class="hero-photo" role="img" aria-label="Photo of a young entrepreneur on the phone, tinted blue-green"></div>
    <h1 class="hero-title">Start your subscription through Vexora.app</h1>
    <p class="hero-lead">Lorem ipsum dolor sit amet, consectetur adipiscing ornare dolor, sed venenatis leo. Integer</p>
    <div class="hero-rule"></div>
    <a class="hero-button">Get Started</a>
  </section>
  <div class="app-preview" role="img" aria-label="Smartphone showing the Vexora app splash screen"></div>

  <section class="about">
    <h2 class="about-title">About us</h2>
    <p class="about-text">Vexora is built to help anyone sort through the confusion of taking an idea from thoughts to a tangible reality, legally.<br>We are here to help make the incorporation, idea protection and any other legal necessities an after thought<br>for you. If you know your idea is the next Pindleco we will help you make the right legal decisions from the start.</p>
  </section>

  <section class="plans">
    <article class="plan-card">
      <h3 class="plan-price">Packages: 2.99</h3>
      <div class="plan-rule"></div>
      <p class="plan-text">Vexora is built to help<br>We are here to<br>for you. If you know</p>
      <p class="plan-term">Valid 30 Day</p>
      <a class="plan-button">Start Now!</a>
    </article>
    <article class="plan-card">
      <h3 class="plan-price">Packages: 2.99</h3>
      <div class="plan-rule"></div>
      <p class="plan-text">Vexora is built to help<br>We are here to<br>for you. If you know</p>
      <p class="plan-term">Valid 30 Day</p>
      <a class="plan-button">Start Now!</a>
    </article>
    <article class="plan-card">
      <h3 class="plan-price">Packages: 2.99</h3>
      <div class="plan-rule"></div>
      <p class="plan-text">Vexora is built to help<br>We are here to<br>for you. If you know</p>
      <p class="plan-term">Valid 30 Day</p>
      <a class="plan-button">Start Now!</a>
    </article>
  </section>

  <footer class="site-footer">
    <div class="footer-brand">
      <span class="footer-brand-dot"></span>
      <span class="footer-brand-name">Vexora</span>
    </div>
    <nav class="footer-nav">
      <a href="#">Home</a>
      <a href="#">Our Team</a>
      <a href="#">Contact Us</a>
    </nav>
    <div class="social">
      <p class="social-label">Follow us on:</p>
      <div class="social-links">
        <span></span><span class="is-active"></span><span></span><span></span>
      </div>
    </div>
  </footer>
</body>
</html>
```